Horse related business entrepreneur needs a business card

I need a business card design for my horse related business. The enterprise is Copper Vale LLC and I have 3 businesses (headquartered at 2 locations): 1. property management where we rent horse stalls and apartments at a thoroughbred training center outside Ocala; 2. a medium sized transportation service in central Florida that sells horse bedding and removes used horse bedding from horse farms; and horse racing

```html
<!DOCTYPE html>
<html lang="en">
<head>
<meta charset="utf-8">
<title>Copper Vale Farm — Business Card</title>
<link href="https://fonts.googleapis.com/css2?family=Roboto:wght@400;500&display=swap" rel="stylesheet">
<style>
  :root {
    --navy: #1d5570;
    --navy-deep: #10506b;
    --copper: #cc6239;
    --paper: #efefed;
    --white: #ffffff;
    --stage: #2a2b2e;
    --photo-light: #e4e6e4;
    --photo-mid: #c9cdc8;
  }
  * { margin: 0; padding: 0; box-sizing: border-box; }
  html, body { width: 1200px; height: 1200px; overflow: hidden; }
  body { background: var(--stage); position: relative; font-family: "Roboto", Arial, sans-serif; }

  .card {
    position: absolute;
    left: 246px;
    width: 886px;
    height: 506px;
    transform: scale(0.8);
    transform-origin: 0 0;
    overflow: hidden;
    box-shadow: 0 10px 30px rgba(0,0,0,.45);
  }
  .card--front { top: 170px; background: var(--paper); }
  .card--back { top: 622px; }

  .front-shape { position: absolute; inset: 0; width: 886px; height: 506px; }

  .brand-name {
    position: absolute;
    font-family: "Roboto", Arial, sans-serif;
    font-weight: 500;
    color: var(--navy);
    white-space: nowrap;
    text-align: center;
  }
  .brand-tagline {
    position: absolute;
    font-family: "Roboto", Arial, sans-serif;
    font-weight: 400;
    color: var(--copper);
    white-space: nowrap;
    text-align: center;
  }
  .card--front .brand-name { left: 0; width: 465px; top: 268px; font-size: 34px; }
  .card--front .brand-tagline { left: 0; width: 465px; top: 314px; font-size: 18px; }

  .contact-person { position: absolute; left: 568px; top: 146px; color: var(--white); }
  .contact-person__name { font-weight: 500; font-size: 31px; line-height: 1.1; }
  .contact-person__role { font-size: 23px; line-height: 1.1; }

  .contact-list { position: absolute; left: 568px; top: 259px; list-style: none; color: var(--white); }
  .contact-list li { display: flex; align-items: center; height: 30px; font-size: 23px; }
  .contact-list svg { width: 18px; height: 18px; margin-right: 16px; flex: none; }

  .back-photo {
    position: absolute; inset: 0;
    background: linear-gradient(180deg, var(--photo-light) 0%, var(--photo-mid) 45%, var(--photo-light) 100%);
  }
  .card--back .brand-name { left: 0; width: 886px; top: 240px; font-size: 48px; }
  .card--back .brand-tagline { left: 0; width: 886px; top: 306px; font-size: 25px; }

  .address-band {
    position: absolute; top: 404px; height: 74px;
    color: var(--white); font-size: 20px; line-height: 26px;
    padding-top: 12px;
  }
  .address-band--primary { left: 0; width: 438px; background: var(--copper); padding-left: 148px; }
  .address-band--secondary { left: 447px; width: 439px; background: var(--navy-deep); padding-left: 56px; }
</style>
</head>
<body>

<section class="card card--front">
  <svg class="front-shape" viewBox="0 0 886 506">
    <path role="img" aria-label="Faded blue-tinted photo of horses and riders at a training track" d="M410 0 Q560 250 400 506 L886 506 L886 0 Z" fill="#1d5570"/>
    <path d="M402 0 Q538 250 344 506 L392 506 Q548 250 406 0 Z" fill="#cc6239"/>
  </svg>
  <div class="brand-name">Copper Vale Farm</div>
  <div class="brand-tagline">Horse Boarding · Pine Hollow</div>

  <div class="contact-person">
    <div class="contact-person__name">Dale Hartwell</div>
    <div class="contact-person__role">Owner</div>
  </div>
  <ul class="contact-list">
    <li><svg viewBox="0 0 24 24" fill="none" stroke="#fff" stroke-width="2"><path d="M5 3h4l2 5-3 2a12 12 0 0 0 6 6l2-3 5 2v4a2 2 0 0 1-2 2A17 17 0 0 1 3 5a2 2 0 0 1 2-2z"/></svg>(352) 555-0147</li>
    <li><svg viewBox="0 0 24 24" fill="#fff"><rect x="6" y="2" width="12" height="6"/><rect x="2" y="9" width="20" height="9" rx="2"/><rect x="6" y="15" width="12" height="7" fill="#fff" stroke="#1d5570" stroke-width="1.5"/></svg>(352) 555-0188</li>
    <li><svg viewBox="0 0 24 24" fill="none" stroke="#fff" stroke-width="2"><rect x="2" y="5" width="20" height="14"/><path d="M2 5l10 8 10-8"/></svg>dale@coppervale.com</li>
    <li><svg viewBox="0 0 24 24" fill="none" stroke="#fff" stroke-width="2"><circle cx="12" cy="12" r="10"/><ellipse cx="12" cy="12" rx="4" ry="10"/><path d="M2 12h20M4 7h16M4 17h16"/></svg>www.coppervale.com</li>
  </ul>
</section>

<section class="card card--back">
  <div class="back-photo" role="img" aria-label="Faded photo of a misty thoroughbred training track with horses, riders and white rails"></div>
  <div class="brand-name">Copper Vale Farm</div>
  <div class="brand-tagline">Horse Boarding · Pine Hollow</div>
  <div class="address-band address-band--primary">1820 Willow Ridge Lane<br>Fern Hollow, GA 30999</div>
  <div class="address-band address-band--secondary">2750 SE 131st Court<br>Pine Hollow, FL 34999</div>
</section>

</body>
</html>
```